Zielgruppe
Wir sind ein Fliesenlegerbetrieb und sind auf der suche nach Mitarbeitern / Fliesenleger. Unsere Kunden sind Privatkunden sowie Öffentliche und Gewerbliche Auftraggeber. Das design soll für Arbeitsuchende ansprechend sein und zu unserem CI passen. Inspiration zu unserem CI finden SIe unter www.fliesen-worlak.de
Aufgabenstellung
Es handelt sich um eine Stellenanzeige die wir im Format 90x50 mm quer und im Format 90 x 90 mm benötigen. In Farbe und S/W.
Unser Textvorschlag, Der Designer darf aucg selbst kreativ sein / werden.
Du arbeitest selbständig und verantwortungsbewusst, hast Freude am Kundenkontakt und kannst jedes Problem lösen ? Dann komm direkt zu uns !
Das erwartet Dich bei uns:
- Junges eingespieltes Team
- Sehr gutes Betriebsklima
- Faire Bezahlung
- Baustellenfahrzeug + Werkzeug
- Unbefristetes Arbeitsverhältnis
- Heimatnahe Baustellen
- Öffentliche, Gewerbliche, Private Baustellen
Kontaktdaden damit sich der Bewerber auch bei uns melden kann !

```html
<!DOCTYPE html>
<html lang="de">
<head>
<meta charset="utf-8">
<title>Stellenanzeige Fliesenleger – Fliesen-Worlak</title>
<link href="https://fonts.googleapis.com/css2?family=Roboto:wght@400;500;700;900&family=Roboto+Condensed:wght@500;700&display=swap" rel="stylesheet">
<style>
  :root{
    --red:#d20a11;
    --black:#000;
    --ink:#1a1a1a;
    --white:#fff;
    --page:#fff;
  }
  *{box-sizing:border-box;margin:0;padding:0}
  html,body{width:1200px;height:975px;overflow:hidden;background:var(--page)}
  body{position:relative;font-family:"Roboto",Arial,sans-serif;color:var(--white)}

  .ad{position:absolute;overflow:hidden}
  .ad.is-color{--accent:var(--red)}
  .ad.is-mono{--accent:var(--black)}
  .ad--square{width:509px;height:509px;top:60px}
  .ad--wide{width:510px;height:284px;top:625px}
  .pos-left{left:58px}
  .pos-right{left:631px}

  .photo{position:absolute;inset:0}
  .is-color .photo{background:
    radial-gradient(ellipse at 30% 45%, #e9e4df 0%, #cdbfb3 30%, transparent 55%),
    linear-gradient(160deg,#8a6a58 0%,#c9b3a3 35%,#e7ddd4 55%,#b7a08f 75%,#5e4334 100%)}
  .is-mono .photo{background:
    radial-gradient(ellipse at 30% 45%, #ececec 0%, #c4c4c4 30%, transparent 55%),
    linear-gradient(160deg,#555 0%,#b5b5b5 35%,#e6e6e6 55%,#a0a0a0 75%,#2e2e2e 100%)}
  .ad--wide .photo::after{content:"";position:absolute;inset:0;
    background:linear-gradient(90deg,transparent 35%,rgba(255,255,255,.9) 60%,rgba(255,255,255,.95) 100%)}

  .logo-box{position:absolute;background:var(--white);display:flex;align-items:center;justify-content:center}
  .logo-name{font-family:"Roboto",Arial,sans-serif;font-weight:700;color:var(--ink);letter-spacing:.2px}
  .ad--square .logo-box{left:276px;top:0;width:233px;height:88px}
  .ad--square .logo-name{font-size:27px;margin-top:14px}
  .ad--wide .logo-box{left:323px;top:213px;width:187px;height:71px}
  .ad--wide .logo-name{font-size:21px;margin-top:10px}

  .headline{position:absolute;color:var(--accent);line-height:.95;letter-spacing:-1.5px}
  .headline .light{font-weight:400}
  .headline .bold{font-weight:900;letter-spacing:-2.5px}
  .ad--square .headline{left:0;width:509px;top:104px;text-align:center}
  .ad--square .headline .light{display:block;font-size:49px;padding-left:4px}
  .ad--square .headline .bold{display:block;font-size:49px;margin-top:2px}
  .ad--wide .headline{right:12px;top:14px;font-size:37px;white-space:nowrap}

  .pitch{position:absolute;background:var(--accent);color:var(--white);font-weight:400}
  .pitch b{font-weight:700}
  .ad--square .pitch{left:250px;top:216px;width:259px;height:145px;padding:16px 14px 0 22px;font-size:18px;line-height:21.6px}
  .ad--wide .pitch{left:191px;top:61px;width:319px;height:60px;padding:4px 6px 0 13px;font-size:13.3px;line-height:17px;letter-spacing:-.1px}
  .ad--wide .pitch .line{display:block;white-space:nowrap}

  .perks-title{position:absolute;font-family:"Roboto Condensed","Roboto",sans-serif;font-weight:700}
  .is-color .perks-title{color:var(--red)}
  .ad--square.is-mono .perks-title{color:var(--white)}
  .ad--wide.is-mono .perks-title{color:var(--ink)}
  .ad--square .perks-title{left:44px;top:370px;font-size:16px}
  .ad--wide .perks-title{left:202px;top:131px;font-size:14.5px}

  .perks{position:absolute;list-style:none}
  .perks li{display:inline;white-space:nowrap}
  .perks li::before{content:"✓";margin-right:3px}
  .is-color .perks li::before{color:var(--red)}
  .ad--square .perks{left:20px;width:470px;top:395px;font-size:12.4px;line-height:13.6px;text-align:center;color:var(--white)}
  .ad--square.is-mono .perks li::before{color:var(--white)}
  .ad--wide .perks{left:202px;width:300px;top:152px;font-size:11.2px;line-height:13px;color:var(--ink)}
  .ad--wide.is-mono .perks li::before{color:var(--ink)}
  .perks .br{display:block;height:0}

  .contact{position:absolute;display:flex;align-items:center;justify-content:center;background:var(--accent);color:var(--white);white-space:nowrap}
  .contact svg{flex:none;fill:var(--white)}
  .contact b{font-weight:700}
  .ad--square .contact{top:451px;height:35px;font-size:15.5px}
  .ad--square .contact svg{width:18px;height:18px;margin-right:10px}
  .ad--square .contact--mail{left:50px;width:210px}
  .ad--square .contact--phone{left:270px;width:188px}
  .ad--wide .contact{top:247px;height:27px;font-size:11.5px}
  .ad--wide .contact svg{width:13px;height:13px;margin-right:7px}
  .ad--wide .contact--mail{left:11px;width:158px}
  .ad--wide .contact--phone{left:177px;width:138px}
</style>
</head>
<body>

<!-- Quadratisch, Farbe -->
<article class="ad ad--square is-color pos-left">
  <div class="photo" role="img" aria-label="Foto: Hand mit Arbeitshandschuh verlegt eine Fliese"></div>
  <div class="logo-box"><span class="logo-name">Fliesen-Worlak</span></div>
  <h1 class="headline"><span class="light">Fliesenleger</span><span class="bold">gesucht!</span></h1>
  <p class="pitch">Du arbeitest <b>selbständig</b> und <b>verantwortungsbe-<br>wusst</b>, hast <b>Freude</b> am Kundenkontakt und kannst jedes Problem lösen?</p>
  <h2 class="perks-title">Das erwartet Dich bei uns</h2>
  <ul class="perks">
    <li>Junges eingespieltes Team</li> <li>Sehr gutes Betriebsklima</li> <li>Faire Bezahlung</li><span class="br"></span>
    <li>Baustellenfahrzeug + Werkzeug</li> <li>Unbefristetes Arbeitsverhältnis</li><span class="br"></span>
    <li>Heimatnahe Baustellen</li> <li>Öffentliche, Gewerbliche Private Baustellen</li>
  </ul>
  <div class="contact contact--mail"><svg viewBox="0 0 24 24"><path d="M2 6.5l10 7.5 10-7.5V19H2z"/><path d="M2 5h20l-10 7.5z"/></svg><span>info@<b>fliesen-worlak.de</b></span></div>
  <div class="contact contact--phone"><svg viewBox="0 0 24 24"><path d="M6.6 10.8a15.1 15.1 0 0 0 6.6 6.6l2.2-2.2a1 1 0 0 1 1-.25 11.4 11.4 0 0 0 3.6.57 1 1 0 0 1 1 1V20a1 1 0 0 1-1 1A17 17 0 0 1 3 4a1 1 0 0 1 1-1h3.5a1 1 0 0 1 1 1c0 1.25.2 2.45.57 3.6a1 1 0 0 1-.25 1z"/></svg><span>(09123) <b>4 56 78 90</b></span></div>
</article>

<!-- Quadratisch, S/W -->
<article class="ad ad--square is-mono pos-right">
  <div class="photo" role="img" aria-label="Foto: Hand mit Arbeitshandschuh verlegt eine Fliese, schwarzweiß"></div>
  <div class="logo-box"><span class="logo-name">Fliesen-Worlak</span></div>
  <h1 class="headline"><span class="light">Fliesenleger</span><span class="bold">gesucht!</span></h1>
  <p class="pitch">Du arbeitest <b>selbständig</b> und <b>verantwortungsbe-<br>wusst</b>, hast <b>Freude</b> am Kundenkontakt und kannst jedes Problem lösen?</p>
  <h2 class="perks-title">Das erwartet Dich bei uns</h2>
  <ul class="perks">
    <li>Junges eingespieltes Team</li> <li>Sehr gutes Betriebsklima</li> <li>Faire Bezahlung</li><span class="br"></span>
    <li>Baustellenfahrzeug + Werkzeug</li> <li>Unbefristetes Arbeitsverhältnis</li><span class="br"></span>
    <li>Heimatnahe Baustellen</li> <li>Öffentliche, Gewerbliche Private Baustellen</li>
  </ul>
  <div class="contact contact--mail"><svg viewBox="0 0 24 24"><path d="M2 6.5l10 7.5 10-7.5V19H2z"/><path d="M2 5h20l-10 7.5z"/></svg><span>info@<b>fliesen-worlak.de</b></span></div>
  <div class="contact contact--phone"><svg viewBox="0 0 24 24"><path d="M6.6 10.8a15.1 15.1 0 0 0 6.6 6.6l2.2-2.2a1 1 0 0 1 1-.25 11.4 11.4 0 0 0 3.6.57 1 1 0 0 1 1 1V20a1 1 0 0 1-1 1A17 17 0 0 1 3 4a1 1 0 0 1 1-1h3.5a1 1 0 0 1 1 1c0 1.25.2 2.45.57 3.6a1 1 0 0 1-.25 1z"/></svg><span>(09123) <b>4 56 78 90</b></span></div>
</article>

<!-- Quer, Farbe -->
<article class="ad ad--wide is-color pos-left">
  <div class="photo" role="img" aria-label="Foto: Hand mit Arbeitshandschuh verlegt eine Fliese"></div>
  <h1 class="headline"><span class="light">Fliesenleger</span> <span class="bold">gesucht!</span></h1>
  <p class="pitch"><span class="line">Du arbeitest <b>selbständig</b> und <b>verantwortungs-</b></span><span class="line"><b>bewusst</b>, hast <b>Freude</b> am Kundenkontakt und</span><span class="line">kannst jedes Problem lösen?</span></p>
  <h2 class="perks-title">Das erwartet Dich bei uns</h2>
  <ul class="perks">
    <li>Junges eingespieltes Team</li> <li>Sehr gutes Betriebsklima</li><span class="br"></span>
    <li>Faire Bezahlung</li> <li>Baustellenfahrzeug + Werkzeug</li><span class="br"></span>
    <li>Unbefristetes Arbeitsverhältnis</li> <li>Heimatnahe Baustellen</li><span class="br"></span>
    <li>Öffentliche, Gewerbliche Private Baustellen</li>
  </ul>
  <div class="logo-box"><span class="logo-name">Fliesen-Worlak</span></div>
  <div class="contact contact--mail"><svg viewBox="0 0 24 24"><path d="M2 6.5l10 7.5 10-7.5V19H2z"/><path d="M2 5h20l-10 7.5z"/></svg><span>info@<b>fliesen-worlak.de</b></span></div>
  <div class="contact contact--phone"><svg viewBox="0 0 24 24"><path d="M6.6 10.8a15.1 15.1 0 0 0 6.6 6.6l2.2-2.2a1 1 0 0 1 1-.25 11.4 11.4 0 0 0 3.6.57 1 1 0 0 1 1 1V20a1 1 0 0 1-1 1A17 17 0 0 1 3 4a1 1 0 0 1 1-1h3.5a1 1 0 0 1 1 1c0 1.25.2 2.45.57 3.6a1 1 0 0 1-.25 1z"/></svg><span>(09123) <b>4 56 78 90</b></span></div>
</article>

<!-- Quer, S/W -->
<article class="ad ad--wide is-mono pos-right">
  <div class="photo" role="img" aria-label="Foto: Hand mit Arbeitshandschuh verlegt eine Fliese, schwarzweiß"></div>
  <h1 class="headline"><span class="light">Fliesenleger</span> <span class="bold">gesucht!</span></h1>
  <p class="pitch"><span class="line">Du arbeitest <b>selbständig</b> und <b>verantwortungs-</b></span><span class="line"><b>bewusst</b>, hast <b>Freude</b> am Kundenkontakt und</span><span class="line">kannst jedes Problem lösen?</span></p>
  <h2 class="perks-title">Das erwartet Dich bei uns</h2>
  <ul class="perks">
    <li>Junges eingespieltes Team</li> <li>Sehr gutes Betriebsklima</li><span class="br"></span>
    <li>Faire Bezahlung</li> <li>Baustellenfahrzeug + Werkzeug</li><span class="br"></span>
    <li>Unbefristetes Arbeitsverhältnis</li> <li>Heimatnahe Baustellen</li><span class="br"></span>
    <li>Öffentliche, Gewerbliche Private Baustellen</li>
  </ul>
  <div class="logo-box"><span class="logo-name">Fliesen-Worlak</span></div>
  <div class="contact contact--mail"><svg viewBox="0 0 24 24"><path d="M2 6.5l10 7.5 10-7.5V19H2z"/><path d="M2 5h20l-10 7.5z"/></svg><span>info@<b>fliesen-worlak.de</b></span></div>
  <div class="contact contact--phone"><svg viewBox="0 0 24 24"><path d="M6.6 10.8a15.1 15.1 0 0 0 6.6 6.6l2.2-2.2a1 1 0 0 1 1-.25 11.4 11.4 0 0 0 3.6.57 1 1 0 0 1 1 1V20a1 1 0 0 1-1 1A17 17 0 0 1 3 4a1 1 0 0 1 1-1h3.5a1 1 0 0 1 1 1c0 1.25.2 2.45.57 3.6a1 1 0 0 1-.25 1z"/></svg><span>(09123) <b>4 56 78 90</b></span></div>
</article>

</body>
</html>
```